Reed & Vale NC grand opening (for BILLBOARD)

Advertising the grand opening of our cannabis/hemp shop in NC. We will sell all things hemp (flower, cartridges, disposables, edibles, creams, lotions, pet products etc...)

Requirements
Must have
• include, open starting Aug 1, but grand opening Aug 15th.
Nice to have
• Difference slogan ideas "Save some cash, buy our grass" "Find your perfect high at Reed & Vale cannabis store" "Experience Nature's Gift: Reed & Vale Cannabis Store"

```html
<!DOCTYPE html>
<html lang="en">
<head>
<meta charset="UTF-8">
<title>Reed &amp; Vale — Billboard</title>
<link rel="stylesheet" href="https://fonts.googleapis.com/css2?family=Montserrat:wght@600;800&display=swap">
<style>
  :root {
    --forest: #03603a;
    --forest-deep: #02502f;
    --leaf: #6cbd3c;
    --leaf-bright: #79c143;
    --board: #f8f8f5;
    --ink: #03603a;
    --stage: #e9ecea;
  }
  * { margin: 0; padding: 0; box-sizing: border-box; }
  html, body {
    width: 1200px;
    height: 900px;
    overflow: hidden;
    background: var(--stage);
  }
  .billboard {
    position: absolute;
    left: 40px;
    top: 207px;
    width: 1120px;
    height: 486px;
    background: var(--board);
    overflow: hidden;
    font-family: "Montserrat", sans-serif;
  }
  .billboard__swooshes {
    position: absolute;
    inset: 0;
    width: 100%;
    height: 100%;
  }
  .billboard__content {
    position: absolute;
    left: 235px;
    width: 720px;
    top: 0;
    height: 100%;
    text-align: center;
  }
  .brand-name {
    position: absolute;
    top: 78px;
    left: 0;
    right: 0;
    font-weight: 600;
    font-size: 46px;
    line-height: 56px;
    letter-spacing: -0.5px;
    color: var(--ink);
  }
  .headline {
    position: absolute;
    top: 150px;
    left: 0;
    right: 0;
    font-weight: 800;
    font-size: 64px;
    line-height: 76px;
    letter-spacing: -1px;
    color: var(--ink);
    text-transform: uppercase;
  }
  .headline__accent { color: var(--leaf); }
  .opening-dates {
    position: absolute;
    top: 318px;
    left: 0;
    right: 0;
    font-weight: 800;
    font-size: 24px;
    line-height: 32px;
    letter-spacing: 0.5px;
    color: var(--ink);
    text-transform: uppercase;
  }
  .opening-dates__accent { color: var(--leaf); }
  .location {
    position: absolute;
    top: 392px;
    left: 0;
    right: 0;
    display: flex;
    justify-content: center;
    align-items: center;
    gap: 16px;
    font-weight: 800;
    font-size: 30px;
    letter-spacing: 0.5px;
    color: var(--ink);
    text-transform: uppercase;
  }
  .location__pin { width: 30px; height: 42px; }
</style>
</head>
<body>
  <section class="billboard" aria-label="Reed &amp; Vale billboard">
    <svg class="billboard__swooshes" viewBox="0 0 1120 486" preserveAspectRatio="none" aria-hidden="true">
      <path d="M0 0 H430 C230 40 60 220 0 450 Z" fill="var(--leaf-bright)"/>
      <path d="M0 0 H400 C210 45 40 205 0 335 Z" fill="var(--board)"/>
      <path d="M0 0 H392 C204 46 34 198 0 322 Z" fill="var(--forest)"/>
      <path d="M0 0 H250 C120 50 30 150 0 250 Z" fill="var(--forest-deep)" opacity="0.35"/>
      <path d="M1120 60 C1060 300 960 430 820 486 H1120 Z" fill="var(--leaf-bright)"/>
      <path d="M1120 150 C1070 330 980 445 862 486 H1120 Z" fill="var(--board)"/>
      <path d="M1120 158 C1072 338 984 450 872 486 H1120 Z" fill="var(--forest)"/>
      <path d="M1120 250 C1080 380 1010 460 960 486 H1120 Z" fill="var(--forest-deep)" opacity="0.35"/>
    </svg>

    <div class="billboard__content">
      <div class="brand-name">Reed &amp; Vale</div>
      <h1 class="headline">
        Save some <span class="headline__accent">cash,</span><br>
        Buy our <span class="headline__accent">grass</span>
      </h1>
      <p class="opening-dates">
        Open Aug 1 &middot; <span class="opening-dates__accent">Grand Opening Aug 15</span>
      </p>
      <p class="location">
        <svg class="location__pin" viewBox="0 0 30 42" aria-hidden="true">
          <path d="M15 1 C7 1 1 7 1 15 C1 25 15 41 15 41 C15 41 29 25 29 15 C29 7 23 1 15 1 Z" fill="var(--leaf)"/>
          <circle cx="15" cy="15" r="6" fill="var(--board)"/>
        </svg>
        Exit 9B Millbrook Rd
      </p>
    </div>
  </section>
</body>
</html>
```